The Brightwater Compass Business Card

We need an attractive business card with the logo that we bought from ArtVantly last year.
Our mission is to contribute to change the way today's leaders manage business companies bringing value to the workplace and helping them to build a new model of creating wealth.
Our logo is clear about our values : we seek Positive Change through People and are convinced that the pursuit of individual well-being and the chase of economic results can converge with the right management.
Management Consulting
Corinne Fabrelle
+34 612 98 70 31
corinne.fabrelle@thebrightwatercompass-mail.net
www.thebrightwatercompass-mail.net

```html
<!DOCTYPE html>
<html lang="en">
<head>
<meta charset="utf-8">
<title>The Brightwater Compass – Business Card</title>
<link rel="stylesheet" href="https://fonts.googleapis.com/css2?family=Marcellus&family=Open+Sans:wght@400&display=swap">
<style>
  :root {
    --backdrop: #c9c9cc;
    --teal: #128c88;
    --teal-deep: #0e7773;
    --card-white: #ffffff;
    --ink: #4a4a4a;
  }
  * { margin: 0; padding: 0; box-sizing: border-box; }
  html, body {
    width: 1200px;
    height: 1200px;
    overflow: hidden;
    background: var(--backdrop);
  }
  .sheet {
    width: 1200px;
    height: 1200px;
    display: flex;
    flex-direction: column;
    align-items: center;
    justify-content: center;
    gap: 60px;
  }
  .card {
    width: 840px;
    height: 480px;
    position: relative;
  }
  .card--back {
    background: var(--teal);
    display: flex;
    align-items: center;
    justify-content: center;
  }
  .card--front {
    background: var(--card-white);
  }
  .wordmark {
    font-family: "Marcellus", serif;
    text-transform: uppercase;
    letter-spacing: 1px;
    text-align: center;
    line-height: 1.1;
  }
  .card--back .wordmark {
    color: var(--teal-deep);
    font-size: 44px;
  }
  .card--front .wordmark {
    position: absolute;
    top: 70px;
    right: 60px;
    color: var(--teal);
    font-size: 32px;
  }
  .holder {
    position: absolute;
    left: 70px;
    bottom: 70px;
  }
  .holder__name {
    font-family: "Marcellus", serif;
    text-transform: uppercase;
    color: var(--teal);
    font-size: 30px;
    letter-spacing: 1px;
  }
  .holder__role {
    font-family: "Open Sans", sans-serif;
    color: var(--ink);
    font-size: 20px;
    margin-bottom: 26px;
  }
  .contact {
    list-style: none;
    font-family: "Open Sans", sans-serif;
    color: var(--ink);
    font-size: 20px;
  }
  .contact li {
    display: flex;
    align-items: center;
    gap: 14px;
    line-height: 1.5;
  }
  .contact svg { width: 18px; height: 18px; fill: var(--teal); flex: none; }
</style>
</head>
<body>
  <main class="sheet">
    <section class="card card--back" aria-label="Card back">
      <p class="wordmark">The Brightwater<br>Compass</p>
    </section>

    <section class="card card--front" aria-label="Card front">
      <p class="wordmark">The Brightwater<br>Compass</p>

      <div class="holder">
        <h1 class="holder__name">Corinne Fabrelle</h1>
        <p class="holder__role">President</p>
        <ul class="contact">
          <li>
            <svg viewBox="0 0 24 24" aria-hidden="true"><path d="M6.6 10.8a15.1 15.1 0 0 0 6.6 6.6l2.2-2.2c.3-.3.7-.4 1-.2 1.1.4 2.3.6 3.6.6.6 0 1 .4 1 1V20c0 .6-.4 1-1 1A17 17 0 0 1 3 4c0-.6.4-1 1-1h3.5c.6 0 1 .4 1 1 0 1.3.2 2.5.6 3.6.1.3 0 .7-.2 1z"/></svg>
            <span>+34 612 98 70 31</span>
          </li>
          <li>
            <svg viewBox="0 0 24 24" aria-hidden="true"><path d="M2 5h20v14H2z M2 5l10 8 10-8" /></svg>
            <span>corinne.fabrelle@thebrightwatercompass-mail.net</span>
          </li>
          <li>
            <svg viewBox="0 0 24 24" aria-hidden="true"><circle cx="12" cy="12" r="10"/></svg>
            <span>www.thebrightwatercompass-mail.net</span>
          </li>
        </ul>
      </div>
    </section>
  </main>
</body>
</html>
```